Web Design Project for velbrook

We are looking for a sleek and sophisticated website design for our already developed web-based gallery management software application. Here is a link to our web-app: http://www.vel-brook.co

You will login on the main page and then we would like to include all of the information on the PDF that I am providing below (it outlines what?, where?, why? who? and how much?). Basically, we need a home page, about page, and a pricing page, as well as a sign up page that should be navigable from the upper right hand corner of the site where the sign in/sign up would be located. Also, our 3 tenets are that the software program is "attractive, accessible, and affordable", which might need to be somehow incorporated. There are a few websites that we would like for you to take inspiration from listed below:

https://tidemoxen.com (for homepage)
https://plumwovenly.com (for homepage/pricing page/etc)
https://tidemoxen.com/tour (for a tour of how the product works)

We are currently having a logo designed and will share that as soon as it is available! Also, let us know if you need photos/screen shots, as we can provide them.

Thanks!

Reason: Extending deadline as we are just now getting designs we would like to see fully developed.

Target Market(s)

art galleries, artists, art collectors, art consultants, museums

Industry/Entity Type

Software

Requirements
Must have
• Home page
About page (or tour through the app)
Pricing page
Sign up page (the more click-throughs to signing up the better)

```html
<!DOCTYPE html>
<html lang="en">
<head>
<meta charset="utf-8">
<title>velbrook — Gallery management made easy</title>
<link rel="stylesheet" href="https://fonts.googleapis.com/css2?family=Roboto:wght@300;400;500;700&display=swap">
<style>
  :root {
    --sky: #3ec0e4;
    --sky-soft: #8fd8ee;
    --white: #ffffff;
    --rule: #ececec;
    --ink: #2a2a2a;
    --photo-warm: #c9a58c;
    --photo-pale: #f1ebe6;
  }
  * { box-sizing: border-box; margin: 0; padding: 0; }
  html, body {
    width: 1200px; height: 640px; overflow: hidden;
    background: var(--white);
    font-family: "Roboto", "Helvetica Neue", Arial, sans-serif;
  }
  .page { position: relative; width: 1200px; height: 640px; }

  .site-header {
    position: absolute; top: 0; left: 0; width: 1200px; height: 57px;
    background: var(--white);
    box-shadow: 0 1px 4px rgba(0,0,0,0.12);
    z-index: 3;
  }
  .header-inner {
    position: absolute; left: 288px; top: 0; width: 625px; height: 57px;
    border-left: 1px solid var(--rule); border-right: 1px solid var(--rule);
  }
  .brand {
    position: absolute; left: 0; top: 0; width: 65px; height: 57px;
    border-right: 1px solid var(--rule);
    display: flex; align-items: center; justify-content: center;
    color: var(--sky); font-size: 13px; font-weight: 500; text-decoration: none;
  }
  .nav-link {
    position: absolute; top: 0; line-height: 57px;
    color: var(--sky); font-size: 11px; text-decoration: none; letter-spacing: 0.2px;
  }
  .nav-home { left: 93px; }
  .nav-about { left: 144px; }
  .nav-pricing { left: 201px; }
  .nav-login { left: 488px; }

  .account-box {
    position: absolute; left: 539px; top: 0; width: 86px; height: 57px;
    border-left: 1px solid var(--rule);
  }
  .account-box .btn-signup {
    position: absolute; left: 8px; top: 20px; width: 70px; height: 20px;
    border-radius: 3px; background: var(--sky); color: var(--white);
    font-size: 11px; font-weight: 500; line-height: 20px;
    text-align: center; text-decoration: none;
  }

  .hero {
    position: absolute; top: 57px; left: 0; width: 1200px; height: 542px;
    background: var(--sky);
  }
  .hero-photo {
    position: absolute; right: 0; top: 0; width: 464px; height: 542px;
    background: linear-gradient(to right, rgba(62,192,228,0) 0%, var(--photo-warm) 30%, var(--photo-pale) 100%);
    opacity: 0.85;
  }
  .hero-copy { position: absolute; left: 288px; top: 234px; color: var(--white); }
  .hero-title { font-size: 18px; font-weight: 400; letter-spacing: 0.2px; }
  .hero-lede { margin-top: 3px; font-size: 11.5px; font-weight: 300; }
  .hero-lede strong { font-weight: 500; }
  .hero-actions { position: absolute; left: 289px; top: 285px; display: flex; gap: 17px; }
  .btn {
    display: block; height: 33px; line-height: 33px; text-align: center;
    font-size: 11px; text-decoration: none; border-radius: 2px;
  }
  .btn-primary { width: 99px; background: var(--white); color: var(--sky); font-weight: 500; }
  .btn-ghost { width: 80px; background: var(--sky-soft); color: var(--white); }

  .scroll-cue {
    position: absolute; left: 581px; top: 578px; width: 38px; height: 38px;
    border-radius: 50%; background: var(--white);
    box-shadow: 0 1px 2px rgba(0,0,0,0.15);
    border-bottom: 1px solid var(--sky);
    display: flex; align-items: center; justify-content: center; z-index: 2;
  }
</style>
</head>
<body>
<div class="page">
  <header class="site-header">
    <div class="header-inner">
      <a class="brand" href="#">velbrook</a>
      <nav class="main-nav">
        <a class="nav-link nav-home" href="#">HOME</a>
        <a class="nav-link nav-about" href="#">ABOUT</a>
        <a class="nav-link nav-pricing" href="#">PRICING</a>
      </nav>
      <a class="nav-link nav-login" href="#">LOGIN</a>
      <div class="account-box">
        <a class="btn-signup" href="#">SIGN UP</a>
      </div>
    </div>
  </header>

  <section class="hero">
    <div class="hero-photo" role="img" aria-label="Portrait photo of a smiling customer in a white shirt looking upward"></div>
    <div class="hero-copy">
      <h1 class="hero-title">GALLERY MANAGEMENT MADE EASY.</h1>
      <p class="hero-lede"><strong>velbrook</strong> is the simplest way to manage your gallery in the cloud.</p>
    </div>
    <div class="hero-actions">
      <a class="btn btn-primary" href="#">LEARN MORE</a>
      <a class="btn btn-ghost" href="#">VIEW DEMO</a>
    </div>
  </section>

  <a class="scroll-cue" href="#" aria-label="Scroll down">
    <svg width="18" height="10" viewBox="0 0 18 10"><path d="M2 2 L9 8 L16 2" fill="none" stroke="var(--ink)" stroke-width="2.6" stroke-linecap="round" stroke-linejoin="round"/></svg>
  </a>
</div>
</body>
</html>
```